Design a website for our summer bar "Velmo"

Dear designers,

We are seeking a creative and talented individual or team to design a website for our summer bar "Velmo". We would like to have an attractive and user-friendly website that perfectly captures the ambiance of our bar.

On the website, we would like to include the following elements:

Photos: Use photos from our Instagram and Facebook pages + see attachment. (@Dunelamp48Vel) to showcase the visual appeal of our bar.
Menu: Ensure that the menu is clear and easy to read, with attractive images of our food and drinks.
Opening hours: Mention the opening hours of our summer bar, so visitors know when they can pay us a visit.
Quotes: Include some inspiring and fun quotes that reflect the relaxed and vibrant atmosphere of our bar.
Important: We want the website to be developed in a WordPress environment so that we can make changes ourselves if needed. Make sure the design is fully prepared for implementation in WordPress.
Extra; Moving objects, we want a site that lives, not just a plain site with no movement, no excitement. We love some action and effects!
Here are some key points to keep in mind while designing:

Create a summery and cheerful look and feel that aligns with the atmosphere of our bar.
Use our branding, which can be found on our Instagram and Facebook pages (@Dunelamp48Vel), as the basis for the color scheme and overall appearance of the website.

Make the website responsive, ensuring it displays well on both desktop and mobile devices.
We are looking forward to seeing your creative proposals! Feel free to reach out if you need any additional information.

Coding

Coded - Design and coding required

Number of Pages Required

1 page

Requirements
Nice to have
• In attachment is a video from the opening. would be nice if this is included in the website. (if it fits the design).

```html
<!DOCTYPE html>
<html lang="en">
<head>
<meta charset="utf-8">
<title>Velmo – Summer Bar</title>
<link href="https://fonts.googleapis.com/css2?family=Cormorant+Garamond:wght@500;600;700&family=Montserrat:wght@400;500;600;700&display=swap" rel="stylesheet">
<style>
:root{
  --bg:#000;
  --panel:#1b1b1b;
  --panel-2:#161616;
  --red:#d10a10;
  --white:#fff;
  --muted:#b9b9b9;
  --dim:#7a7a7a;
  --serif:"Cormorant Garamond",serif;
  --sans:"Montserrat",sans-serif;
}
*{margin:0;padding:0;box-sizing:border-box}
html,body{width:1200px;height:4683px;overflow:hidden;background:var(--bg);color:var(--white);font-family:var(--sans)}
.page{position:relative;width:1200px;height:4683px;overflow:hidden}
.abs{position:absolute}
.photo{position:absolute}
.eyebrow{font-family:var(--sans);font-weight:500;letter-spacing:.38em;font-size:21px}
.title{font-family:var(--serif);font-weight:700;line-height:1;letter-spacing:.02em}
.rule{position:absolute;height:2px;background:var(--red)}
.body-text{font-size:10.5px;line-height:21px;color:var(--muted)}
.btn{position:absolute;display:flex;align-items:center;justify-content:center;font-size:10px;font-weight:700;letter-spacing:.3em;color:var(--white)}
.btn-solid{background:var(--red)}
.btn-line{border:2px solid var(--red)}
.outline-word{position:absolute;font-family:var(--serif);font-weight:600;color:transparent;-webkit-text-stroke:1.4px #9a9a9a;line-height:1;letter-spacing:.02em}

/* header */
.header-line{top:62px;left:0;width:1200px;height:3px;background:var(--red)}
.brand{top:14px;left:116px;width:140px;height:80px;background:#fff;display:flex;align-items:center;justify-content:center;gap:8px}
.brand span{font-family:var(--sans);font-weight:700;font-size:30px;color:#1d2f8c}
.brand i{display:block;width:12px;height:12px;background:var(--red)}
.nav{top:22px;left:309px;display:flex;gap:36px;font-size:10px;color:#ddd;letter-spacing:.02em}
.nav .active{color:#fff;font-weight:600}
.head-icon{top:18px;width:26px;height:26px;border-radius:50%;background:var(--red);display:flex;align-items:center;justify-content:center}

/* hero */
.slide-line{left:82px;width:2px;background:#444}
.slide-count{top:640px;left:60px;font-size:14px;font-weight:600}
.slide-count small{font-size:10px;color:var(--dim);font-weight:400}

/* hours */
.hours{top:862px;left:196px;width:1004px;height:225px;background:var(--panel)}
.hours-label{font-size:18px;color:#ddd;letter-spacing:.02em;line-height:31px}

/* menu cards */
.card{position:absolute;top:1771px;width:255px;height:298px;background:var(--panel);overflow:hidden}
.card-label{position:absolute;top:30px;left:0;width:100%;text-align:center;font-size:14px;letter-spacing:.35em;font-weight:500}
.card-stem{position:absolute;top:58px;left:50%;width:2px;height:22px;background:#bbb}
.arrow-btn{top:2108px;width:50px;height:50px;border:1.5px solid #888;border-radius:50%}

/* footer */
.footer{top:4178px;left:0;width:1200px;height:505px;background:var(--panel-2)}
.field{position:absolute;left:196px;width:255px;background:#0c0c0c;font-size:9px;color:#555;padding:14px 22px;letter-spacing:.05em}
.foot-nav{top:4294px;left:533px;font-size:9.5px;line-height:24.3px;color:#ddd}
.c-icon{left:749px;width:44px;height:44px;border-radius:50%;background:var(--red);display:flex;align-items:center;justify-content:center}
.c-text{left:816px;font-size:11px;color:#ddd;line-height:15px}
.social{top:4494px;width:22px;height:22px;border-radius:50%;background:#fff;display:flex;align-items:center;justify-content:center}
.social i{display:block;width:7px;height:7px;background:#111;border-radius:50%}
.legal{top:4654px;font-size:9px;color:#ccc}
</style>
</head>
<body>
<div class="page">

  <!-- header -->
  <div class="abs header-line"></div>
  <div class="abs brand"><span>Velmo</span><i></i></div>
  <nav class="abs nav">
    <span class="active">HOME</span><span>OVER ONS</span><span>BROODJESBAR</span><span>RESTAURANT</span><span>MENU</span><span>SEMINARS / FEESTZAAL</span><span>OPENING HOURS</span>
  </nav>
  <div class="abs head-icon" style="left:1062px">
    <svg width="12" height="12" viewBox="0 0 24 24"><path fill="#fff" d="M6.6 10.8a15 15 0 0 0 6.6 6.6l2.2-2.2a1 1 0 0 1 1-.25 11.4 11.4 0 0 0 3.6.57 1 1 0 0 1 1 1V20a1 1 0 0 1-1 1A17 17 0 0 1 3 4a1 1 0 0 1 1-1h3.5a1 1 0 0 1 1 1c0 1.25.2 2.45.57 3.57a1 1 0 0 1-.25 1z"/></svg>
  </div>
  <div class="abs head-icon" style="left:1099px">
    <svg width="12" height="12" viewBox="0 0 24 24"><path fill="#fff" d="M22 2 2 10l7 3 3 7z"/></svg>
  </div>

  <!-- hero -->
  <div class="abs slide-line" style="top:238px;height:72px;background:var(--red)"></div>
  <div class="abs slide-line" style="top:340px;height:70px"></div>
  <div class="abs slide-line" style="top:440px;height:70px"></div>
  <div class="abs slide-line" style="top:540px;height:70px"></div>
  <div class="abs slide-count">01 <small>/ 04</small></div>

  <div class="photo" role="img" aria-label="Terrace of the summer bar under a stretched tent at sunset, with tables, lights and a barrel table" style="top:164px;left:196px;width:462px;height:576px;background:linear-gradient(180deg,#7ea7c8 0%,#c7b79a 35%,#6b5338 60%,#2b1f15 100%)"></div>
  <div class="abs eyebrow" style="top:228px;left:585px;font-size:22px;letter-spacing:.42em">WELCOME TO</div>
  <div class="abs title" style="top:270px;left:585px;font-size:100px">VELMO</div>
  <div class="rule" style="top:378px;left:795px;width:203px"></div>
  <p class="abs body-text" style="top:434px;left:694px;width:305px">Lorem Ipsum is simply dummy text of the printing and typesetting industry. Lorem Ipsum has been the industry's standard dummy text ever since the 1500s, when an unknown printer took a galley of type and scrambled it to make a type specimen book. It has survived not only five centuries, but also the leap into electronic typesetting, remaining essentially unchanged.</p>
  <div class="btn btn-solid" style="top:633px;left:694px;width:162px;height:38px">CONTACT US</div>

  <div class="outline-word" style="top:822px;left:866px;font-size:88px">DRINK</div>

  <!-- about background -->
  <div class="photo" role="img" aria-label="Dim interior of the bar with glassware, softly blurred" style="top:1087px;left:0;width:1200px;height:660px;background:radial-gradient(ellipse at 55% 35%,#2a2623 0%,#141210 45%,#000 80%)"></div>

  <!-- opening hours -->
  <div class="abs hours"></div>
  <div class="abs title" style="top:922px;left:275px;font-size:42px;font-weight:600;line-height:44px">OPENING<br>HOURS</div>
  <div class="rule" style="top:1020px;left:275px;width:120px"></div>
  <div class="abs" style="top:922px;left:536px;width:2px;height:102px;background:#888"></div>
  <div class="abs hours-label" style="top:943px;left:587px">MONDAY - FRIDAY<br>05:30-22:00</div>
  <div class="abs hours-label" style="top:943px;left:836px">SATURDAY - SUNDAY<br>08:00-22:00</div>

  <!-- about -->
  <div class="outline-word" style="top:1232px;left:48px;font-size:72px;transform-origin:0 0;transform:rotate(90deg)">DELIGHT</div>
  <div class="abs eyebrow" style="top:1232px;left:0;width:1200px;text-align:center;font-size:22px">ABOUT</div>
  <div class="abs title" style="top:1272px;left:0;width:1200px;text-align:center;font-size:100px">VELMO</div>
  <p class="abs body-text" style="top:1410px;left:269px;width:662px;text-align:center;color:#ccc">Lorem Ipsum is simply dummy text of the printing and typesetting industry. Lorem Ipsum has been the industry's standard dummy text ever since the 1500s, when an unknown printer took a galley of type and scrambled it to make a type specimen book. It has survived not only five centuries, but also the leap into electronic typesetting, remaining essentially unchanged.</p>
  <p class="abs body-text" style="top:1516px;left:269px;width:662px;text-align:center;color:#ccc">It was popularised in the 1960s with the release of Lettrafix sheets containing Lorem Ipsum passages, and more recently with desktop publishing software like Pageform including versions of Lorem Ipsum.</p>
  <div class="btn btn-line" style="top:1593px;left:516px;width:166px;height:40px">READ MORE</div>

  <!-- menu -->
  <div class="abs eyebrow" style="top:1800px;left:196px">OUR</div>
  <div class="abs title" style="top:1836px;left:196px;font-size:54px;font-weight:600;line-height:58px">DELICIOUS<br>MENU</div>
  <div class="rule" style="top:1968px;left:196px;width:203px"></div>
  <div class="btn btn-solid" style="top:2011px;left:196px;width:204px;height:38px">DOWNLOAD PDF</div>

  <div class="card" style="left:540px">
    <div class="card-label">BEERS</div><div class="card-stem"></div>
    <div class="photo" role="img" aria-label="Beer bottle and glass with a golden splash" style="top:95px;left:40px;width:175px;height:200px;background:radial-gradient(ellipse at 50% 55%,#e3a33a 0%,#9a5a12 45%,transparent 75%)"></div>
  </div>
  <div class="card" style="left:814px">
    <div class="card-label">SOFT DRINKS</div><div class="card-stem"></div>
    <div class="photo" role="img" aria-label="Glass of cola with ice splashing" style="top:95px;left:60px;width:135px;height:200px;background:radial-gradient(ellipse at 50% 60%,#b4521f 0%,#5c1c0a 45%,transparent 75%)"></div>
  </div>
  <div class="card" style="left:1089px;width:111px">
    <div class="card-label" style="text-align:left;left:30px">HOT</div>
    <div class="photo" role="img" aria-label="Cup of coffee" style="top:120px;left:40px;width:71px;height:120px;background:radial-gradient(ellipse at 80% 50%,#e8e2d8 0%,#6b4a30 50%,transparent 80%)"></div>
  </div>
  <div class="outline-word" style="top:2052px;left:866px;font-size:80px">DANCE</div>

  <div class="abs arrow-btn" style="left:539px"></div>
  <svg class="abs" style="top:2126px;left:554px" width="44" height="14" viewBox="0 0 44 14"><path d="M44 7H2M8 1 2 7l6 6" stroke="#fff" stroke-width="1.5" fill="none"/></svg>
  <div class="abs arrow-btn" style="left:648px"></div>
  <svg class="abs" style="top:2126px;left:632px" width="44" height="14" viewBox="0 0 44 14"><path d="M0 7h42M36 1l6 6-6 6" stroke="#fff" stroke-width="1.5" fill="none"/></svg>

  <!-- mixology -->
  <div class="photo" role="img" aria-label="Table of bar snacks: onion rings, dips, fried chicken and potatoes" style="top:2309px;left:0;width:1200px;height:582px;background:linear-gradient(180deg,rgba(0,0,0,0) 55%,#000 100%),linear-gradient(90deg,#5a3a24 0%,#8c5f3a 30%,#6a4a34 60%,#3a2a20 100%)"></div>
  <div class="abs" style="top:2385px;left:533px;width:598px;height:357px;background:rgba(70,64,60,.82)"></div>
  <div class="abs eyebrow" style="top:2444px;left:533px;width:530px;text-align:right">DISCOVER THE</div>
  <div class="abs title" style="top:2480px;left:533px;width:530px;text-align:right;font-size:52px;font-weight:600;line-height:57px">EXQUISITE ART<br>OF MIXOLOGY</div>
  <div class="rule" style="top:2612px;left:860px;width:202px"></div>
  <div class="btn btn-solid" style="top:2645px;left:725px;width:162px;height:37px">OUR MENU</div>
  <div class="btn btn-line" style="top:2645px;left:898px;width:164px;height:37px">DAGMENU'S</div>

  <div class="outline-word" style="top:2808px;left:48px;font-size:72px;transform-origin:0 0;transform:rotate(90deg)">SHOTS</div>

  <!-- gallery -->
  <div class="abs eyebrow" style="top:3078px;left:0;width:536px;text-align:right">OUR</div>
  <div class="abs title" style="top:3114px;left:0;width:536px;text-align:right;font-size:54px;font-weight:600">GALLERY</div>
  <div class="rule" style="top:3190px;left:436px;width:100px"></div>

  <div class="photo" role="img" aria-label="Meat skewers being grilled" style="top:3045px;left:611px;width:294px;height:368px;background:linear-gradient(160deg,#6a7b3a 0%,#9a5048 45%,#c9c2bd 100%)"></div>
  <div class="photo" role="img" aria-label="Green beer bottles in a bucket of ice" style="top:3178px;left:931px;width:269px;height:367px;background:linear-gradient(160deg,#eeeeec 0%,#c9d1cc 50%,#3e6a3e 100%)"></div>
  <div class="photo" role="img" aria-label="Bartender pouring a drink at the tap" style="top:3254px;left:291px;width:296px;height:368px;background:linear-gradient(160deg,#b88a4e 0%,#5b4a3a 45%,#1f4752 100%)"></div>
  <div class="photo" role="img" aria-label="Plate of onion rings, fries and sauce" style="top:3436px;left:611px;width:294px;height:369px;background:linear-gradient(160deg,#8a8a3a 0%,#c07436 50%,#6a3a22 100%)"></div>
  <div class="photo" role="img" aria-label="Cocktail with dried orange slice and mint" style="top:3382px;left:0;width:267px;height:367px;background:linear-gradient(160deg,#dce6d8 0%,#6e9a52 45%,#3a5a2a 100%)"></div>
  <div class="photo" role="img" aria-label="Guests relaxing in deck chairs under the tent" style="top:3642px;left:291px;width:296px;height:367px;background:linear-gradient(180deg,#c8a060 0%,#5a4232 50%,#3a3c5a 100%)"></div>
  <p class="abs body-text" style="top:3862px;left:645px;width:272px">Lorem Ipsum is simply dummy text of the printing and typesetting industry. Lorem Ipsum has been the industry's standard dummy text ever since the 1500s, when an unknown printer took a galley of type and scrambled it to make a type specimen book.</p>

  <!-- footer -->
  <div class="abs footer"></div>
  <div class="outline-word" style="top:4118px;left:674px;font-size:82px">TEQUILA</div>

  <div class="abs" style="top:4283px;left:196px;font-size:18px;color:#ddd">CONTACT US NOW</div>
  <div class="field" style="top:4323px;height:29px;padding-top:9px">NAME</div>
  <div class="field" style="top:4365px;height:31px;padding-top:10px">EMAIL</div>
  <div class="field" style="top:4404px;height:120px;padding-top:10px">MESSAGE</div>
  <svg class="abs" style="top:4500px;left:418px" width="16" height="16" viewBox="0 0 24 24"><path fill="var(--red)" d="M22 2 2 10l7 3 3 7z"/></svg>

  <div class="abs foot-nav">HOME<br>OVER ONS<br>BROODJESBAR<br>RESTAURANT<br>PARKING<br>SEMINARIES // FEESTZAAL<br>DAGWINKEL<br>CONTACT</div>

  <div class="abs c-icon" style="top:4292px"><svg width="16" height="16" viewBox="0 0 24 24"><path fill="#fff" d="M6.6 10.8a15 15 0 0 0 6.6 6.6l2.2-2.2a1 1 0 0 1 1-.25 11.4 11.4 0 0 0 3.6.57 1 1 0 0 1 1 1V20a1 1 0 0 1-1 1A17 17 0 0 1 3 4a1 1 0 0 1 1-1h3.5a1 1 0 0 1 1 1c0 1.25.2 2.45.57 3.57a1 1 0 0 1-.25 1z"/></svg></div>
  <div class="abs c-text" style="top:4307px">011 270 593</div>
  <div class="abs c-icon" style="top:4359px"><svg width="15" height="15" viewBox="0 0 24 24"><path fill="#fff" d="M22 2 2 10l7 3 3 7z"/></svg></div>
  <div class="abs c-text" style="top:4374px">HELLO@VELMOBAR.EU</div>
  <div class="abs c-icon" style="top:4423px"><svg width="14" height="18" viewBox="0 0 24 30"><path fill="#fff" d="M12 0a10 10 0 0 0-10 10c0 7.5 10 20 10 20s10-12.5 10-20A10 10 0 0 0 12 0zm0 14a4 4 0 1 1 0-8 4 4 0 0 1 0 8z"/></svg></div>
  <div class="abs c-text" style="top:4430px">ZANDPAD 8<br>4120 LINDEVELD</div>

  <div class="abs social" style="left:749px"><i></i></div>
  <div class="abs social" style="left:782px"><i></i></div>
  <div class="abs social" style="left:814px"><i></i></div>
  <div class="abs social" style="left:847px"><i></i></div>

  <div class="abs legal" style="left:196px">© Copyright © 2023 Velmo. All Rights Reserved.</div>
  <div class="abs legal" style="left:761px;word-spacing:2px">Policies &nbsp;|&nbsp; Privacy policy &nbsp;|&nbsp; Terms &amp; Conditions</div>

</div>
</body>
</html>
```